Looking for updated Letterhead and Compliments Slips to go with our new updated logo. This stationary will be used for letters to suppliers and customers so needs to be practical while also quite classic.

We are an engineering company so needs to be clean and precise

Target Market(s)

SME'S and large automotive customers

Industry/Entity Type

Automotive

Font styles to use
Sans Serif

Colors
85acd3
0356a4
0792cd
33a6d7
85abd2
ffffff

Requirements
Must have
• Address details as below
• KT Fabrications Limited
• Hallmere Road
• Ashvale
• Westmarsh
• LP47 9XZ, UK
• Telephone: +44 (0)1632 960418
• Fax: +44 (0)1632 960733
• Email: sales@ktfabrications.example
• Web: www.ktfabrications.example
Nice to have
• Nice to have some element of being a British Manufacturer

```html
<!DOCTYPE html>
<html lang="en">
<head>
<meta charset="utf-8">
<title>KT Fabrications Stationery</title>
<link href="https://fonts.googleapis.com/css2?family=Montserrat:wght@400;500&display=swap" rel="stylesheet">
<style>
  :root {
    --backdrop: #bbbcc0;
    --paper: #ffffff;
    --brand-blue: #0356a4;
    --deep-blue: #0052a0;
    --navy-mark: #0c3a73;
    --faint-mark: #f1f1f1;
    --ink: #1c2230;
    --rule: #2a2f3a;
  }
  * { margin: 0; padding: 0; box-sizing: border-box; }
  html, body { width: 1200px; height: 746px; overflow: hidden; }
  body {
    position: relative;
    background: var(--backdrop);
    font-family: "Montserrat", sans-serif;
    color: var(--ink);
  }
  .sheet { position: absolute; background: var(--paper); overflow: hidden; }
  .letterhead { left: 37px; top: 37px; width: 520px; height: 673px; }
  .comp-slip { left: 582px; top: 109px; width: 581px; height: 251px; }
  .slip-reverse { left: 582px; top: 385px; width: 581px; height: 252px; background: var(--deep-blue); }

  .brand-bar { position: absolute; left: 0; bottom: 0; width: 100%; height: 6px; background: var(--brand-blue); }

  .wordmark {
    position: absolute; left: 0; width: 100%;
    text-align: center;
    font-weight: 500;
    color: var(--brand-blue);
    letter-spacing: 0.32em;
    text-transform: uppercase;
    white-space: nowrap;
    line-height: 1;
  }
  .wordmark-rule { position: absolute; height: 1px; background: var(--brand-blue); }

  .letterhead .wordmark { top: 106px; font-size: 14px; }
  .letterhead .wordmark-rule { top: 131px; left: 233px; width: 54px; }
  .comp-slip .wordmark { top: 80px; font-size: 12px; }
  .comp-slip .wordmark-rule { top: 101px; left: 268px; width: 46px; }

  .watermark {
    position: absolute; left: 0; width: 100%;
    text-align: center; font-weight: 500;
    letter-spacing: 0.12em; text-transform: uppercase;
    white-space: nowrap;
  }
  .letterhead .watermark { top: 318px; font-size: 38px; color: var(--faint-mark); }
  .slip-reverse .watermark { top: 106px; font-size: 30px; color: var(--navy-mark); }

  .contact { position: absolute; line-height: 1.6; white-space: nowrap; }
  .contact-icon { position: absolute; fill: var(--brand-blue); }
  .divider { position: absolute; width: 1px; background: var(--rule); }

  .letterhead .contact { font-size: 8.5px; top: 610px; }
  .letterhead .contact-icon { width: 8px; height: 8px; }
  .letterhead .divider { top: 607px; height: 28px; }

  .comp-slip .contact { font-size: 7.4px; top: 204px; }
  .comp-slip .contact-icon { width: 7px; height: 7px; }
  .comp-slip .divider { top: 201px; height: 26px; }
</style>
</head>
<body>

<section class="sheet letterhead" aria-label="Letterhead">
  <div class="wordmark">KT Fabrications</div>
  <div class="wordmark-rule"></div>
  <div class="watermark" aria-hidden="true">KT Fabrications</div>

  <svg class="contact-icon" style="left:42px;top:614px" viewBox="0 0 10 10"><path d="M5 0a3.5 3.5 0 0 0-3.5 3.5C1.5 6 5 10 5 10s3.5-4 3.5-6.5A3.5 3.5 0 0 0 5 0zm0 5a1.5 1.5 0 1 1 0-3 1.5 1.5 0 0 1 0 3z"/></svg>
  <p class="contact" style="left:53px">Hallmere Road | Ashvale | Westmarsh<br>LP47 9XZ, UK</p>
  <div class="divider" style="left:221px"></div>

  <svg class="contact-icon" style="left:240px;top:614px" viewBox="0 0 10 10"><path d="M3 0h2v3H4v4h1v3H3C1.5 8 1.5 2 3 0z"/></svg>
  <svg class="contact-icon" style="left:239px;top:628px" viewBox="0 0 10 10"><rect x="2" y="0" width="6" height="3"/><rect x="0" y="3.5" width="10" height="4"/><rect x="2" y="8" width="6" height="2"/></svg>
  <p class="contact" style="left:250px">+44 (0)1632 960418<br>+44 (0)1632 960733</p>
  <div class="divider" style="left:347px"></div>

  <svg class="contact-icon" style="left:366px;top:614px" viewBox="0 0 10 10"><path d="M0 2h10v6H0zM0 2l5 3.5L10 2" stroke="#fff" stroke-width="0.8"/></svg>
  <svg class="contact-icon" style="left:366px;top:628px" viewBox="0 0 10 10"><circle cx="5" cy="5" r="5"/><path d="M1 5h8M5 1c-2 2-2 6 0 8M5 1c2 2 2 6 0 8" stroke="#fff" stroke-width="0.7" fill="none"/></svg>
  <p class="contact" style="left:378px">sales@ktfabrications.example<br>www.ktfabrications.example</p>

  <div class="brand-bar"></div>
</section>

<section class="sheet comp-slip" aria-label="Compliments slip, front">
  <div class="wordmark">KT Fabrications</div>
  <div class="wordmark-rule"></div>

  <svg class="contact-icon" style="left:91px;top:207px" viewBox="0 0 10 10"><path d="M5 0a3.5 3.5 0 0 0-3.5 3.5C1.5 6 5 10 5 10s3.5-4 3.5-6.5A3.5 3.5 0 0 0 5 0zm0 5a1.5 1.5 0 1 1 0-3 1.5 1.5 0 0 1 0 3z"/></svg>
  <p class="contact" style="left:100px">Hallmere Road | Ashvale | Westmarsh<br>LP47 9XZ, UK</p>
  <div class="divider" style="left:255px"></div>

  <svg class="contact-icon" style="left:271px;top:207px" viewBox="0 0 10 10"><path d="M3 0h2v3H4v4h1v3H3C1.5 8 1.5 2 3 0z"/></svg>
  <svg class="contact-icon" style="left:270px;top:219px" viewBox="0 0 10 10"><rect x="2" y="0" width="6" height="3"/><rect x="0" y="3.5" width="10" height="4"/><rect x="2" y="8" width="6" height="2"/></svg>
  <p class="contact" style="left:280px">+44 (0)1632 960418<br>+44 (0)1632 960733</p>
  <div class="divider" style="left:370px"></div>

  <svg class="contact-icon" style="left:385px;top:207px" viewBox="0 0 10 10"><path d="M0 2h10v6H0zM0 2l5 3.5L10 2" stroke="#fff" stroke-width="0.8"/></svg>
  <svg class="contact-icon" style="left:385px;top:219px" viewBox="0 0 10 10"><circle cx="5" cy="5" r="5"/><path d="M1 5h8M5 1c-2 2-2 6 0 8M5 1c2 2 2 6 0 8" stroke="#fff" stroke-width="0.7" fill="none"/></svg>
  <p class="contact" style="left:398px">sales@ktfabrications.example<br>www.ktfabrications.example</p>

  <div class="brand-bar"></div>
</section>

<section class="sheet slip-reverse" aria-label="Compliments slip, reverse">
  <div class="watermark" aria-hidden="true">KT Fabrications</div>
</section>

</body>
</html>
```